Garlic Farm for Farm Sales/Restaurant sales

Need a professional, but appealing to agriculture world. We are selling 27 kinds of Organic Garlic from a farm in Simla,CO. I have uploaded logo and business information-we are going to need a template, because I will need to use it for four separate people.
-We are trying to appeal to Farm to table restaurants
-As well as growers/farmers

Target Market(s)

Agriculture Sales/Restaurants-Organic

Industry/Entity Type

Agriculture

Contact Information for Business Card

Want it to look more unique then your average brimly ink card- I want it to look amazing

Font styles to use
Sans Serif

Colors
0455a3
ec1f27
fbed22
ffffff

Requirements
Must have
• Just be creative
Nice to have
• Colorful
Should not have
• plain

```html
<!DOCTYPE html>
<html lang="en">
<head>
<meta charset="utf-8">
<title>Tall Peak Gourmet Garlic – Business Card</title>
<link rel="stylesheet" href="https://fonts.googleapis.com/css2?family=Open+Sans:wght@400;600;700&display=swap">
<style>
  :root {
    --navy: #0a2d5c;
    --blue: #0455a3;
    --red: #ec1f27;
    --red-deep: #c8102e;
    --yellow: #fbed22;
    --white: #ffffff;
    --ink: #555a60;
    --backdrop: #e9e7e4;
  }
  * { box-sizing: border-box; margin: 0; padding: 0; }
  html, body {
    width: 1200px;
    height: 987px;
    overflow: hidden;
    background: var(--backdrop);
    font-family: "Open Sans", Arial, sans-serif;
  }
  .stage { position: relative; width: 1200px; height: 987px; }

  .card {
    position: absolute;
    left: 293px;
    width: 615px;
    height: 352px;
    box-shadow: 0 2px 6px rgba(0,0,0,0.18);
  }
  .card-front { top: 130px; background: var(--white); }
  .card-back  { top: 506px; background: var(--navy); }

  /* Front: brand */
  .brand-front {
    position: absolute;
    right: 30px;
    top: 40px;
    display: flex;
    flex-direction: column;
    align-items: flex-end;
    gap: 14px;
  }
  .brand-mark {
    width: 96px;
    height: 96px;
    border-radius: 50%;
    background: var(--red-deep);
    margin-right: 70px;
  }
  .brand-name {
    font-weight: 700;
    font-size: 26px;
    color: var(--navy);
    line-height: 1.05;
    text-align: right;
  }
  .brand-name small {
    display: block;
    font-size: 15px;
    font-weight: 700;
    color: var(--navy);
  }

  /* Front: person */
  .person { position: absolute; left: 35px; top: 178px; }
  .person-name {
    font-weight: 600;
    font-size: 21px;
    color: var(--navy);
    letter-spacing: 0.3px;
  }
  .person-role {
    font-size: 15px;
    color: var(--red-deep);
    margin-top: 1px;
  }

  .colour-rule {
    position: absolute;
    left: 35px;
    right: 30px;
    top: 238px;
    display: flex;
    gap: 5px;
  }
  .colour-rule span { flex: 1; height: 3px; }
  .rule-blue { background: var(--navy); }
  .rule-yellow { background: var(--yellow); }
  .rule-red { background: var(--red-deep); }

  .contact-list {
    position: absolute;
    left: 35px;
    top: 258px;
    list-style: none;
  }
  .contact-list li {
    display: flex;
    align-items: center;
    gap: 8px;
    font-size: 15px;
    color: var(--ink);
    height: 23.5px;
  }
  .contact-list svg { width: 14px; height: 14px; fill: var(--navy); }

  .address {
    position: absolute;
    right: 30px;
    top: 282px;
    text-align: right;
    font-size: 15px;
    line-height: 23.5px;
    color: var(--ink);
  }

  /* Back */
  .brand-back {
    position: absolute;
    left: 0; right: 0;
    top: 78px;
    display: flex;
    flex-direction: column;
    align-items: center;
    gap: 14px;
  }
  .brand-back .brand-mark { margin: 0; width: 120px; height: 120px; }
  .brand-back .brand-name { color: var(--white); text-align: center; font-size: 20px; }

  .social-row {
    position: absolute;
    left: 105px;
    right: 140px;
    top: 292px;
    display: flex;
    align-items: center;
    gap: 5px;
  }
  .social-row .hairline { flex: 1; height: 1px; background: rgba(255,255,255,0.7); }
  .social-dot {
    width: 22px;
    height: 22px;
    border-radius: 50%;
    border: 1.5px solid var(--white);
  }
</style>
</head>
<body>
<main class="stage">

  <section class="card card-front" aria-label="Business card front">
    <div class="brand-front">
      <div class="brand-mark" aria-hidden="true"></div>
      <div class="brand-name">Tall Peak<small>Gourmet Garlic</small></div>
    </div>

    <div class="person">
      <h1 class="person-name">OWEN HARDY</h1>
      <p class="person-role">CEO/FOUNDER</p>
    </div>

    <div class="colour-rule" aria-hidden="true">
      <span class="rule-blue"></span>
      <span class="rule-yellow"></span>
      <span class="rule-red"></span>
    </div>

    <ul class="contact-list">
      <li>
        <svg viewBox="0 0 24 24" aria-hidden="true"><path d="M6.6 10.8a15.1 15.1 0 0 0 6.6 6.6l2.2-2.2a1 1 0 0 1 1-.25 11.4 11.4 0 0 0 3.6.57 1 1 0 0 1 1 1V20a1 1 0 0 1-1 1A17 17 0 0 1 3 4a1 1 0 0 1 1-1h3.5a1 1 0 0 1 1 1c0 1.25.2 2.45.57 3.57a1 1 0 0 1-.25 1z"/></svg>
        719-555-0147
      </li>
      <li>
        <svg viewBox="0 0 24 24" aria-hidden="true"><path d="M2 5h20v14H2z M2 5l10 8 10-8" fill="var(--navy)"/><path d="M3 6l9 7 9-7" fill="none" stroke="#fff" stroke-width="1.6"/></svg>
        Nell@TPGarlic.com
      </li>
      <li>
        <svg viewBox="0 0 24 24" aria-hidden="true"><circle cx="12" cy="12" r="10"/><path d="M2 12h20M12 2c3 3 3 17 0 20M12 2c-3 3-3 17 0 20" fill="none" stroke="#fff" stroke-width="1.4"/></svg>
        www.TPGarlic.com
      </li>
    </ul>

    <p class="address">P.O. Box 62 Elmor<br>CO&nbsp;&nbsp;80912</p>
  </section>

  <section class="card card-back" aria-label="Business card back">
    <div class="brand-back">
      <div class="brand-mark" aria-hidden="true"></div>
      <div class="brand-name">Tall Peak Gourmet Garlic</div>
    </div>

    <div class="social-row" aria-hidden="true">
      <span class="hairline"></span>
      <span class="social-dot"></span>
      <span class="social-dot"></span>
      <span class="social-dot"></span>
      <span class="social-dot"></span>
      <span class="hairline"></span>
    </div>
  </section>

</main>
</body>
</html>
```